church business card design

we have a logo and would like our business card to complement the logo. we would prefer the logo in white on a coloured background - probably blue. Under the logo or near it we would have the Words 'Love God. Love people. Follow Jesus.'
We would like some yellow/gold highlights. We like the design by mintaro quill 4821 front of card - https://www.pelvarostudio.com/businesscard-design/contest/5812094

Our church is multicultural, inner city, friendly, warm welcoming and that's the feel we would like. there's also an element of being spontaneous, so a swirl or swoosh might help give that feel. the example card above had some curved shapes on the front of the card for example.
on the second side of the card would have the details of the Senior Pastor and the contact details for the church.
after the business card we would be looking at letterhead and an A5 flyer for printing but also as document templates so we can create invitations etc going forward

```html
<!DOCTYPE html>
<html lang="en">
<head>
<meta charset="utf-8">
<title>Harbor Stone Church – Business Card</title>
<link href="https://fonts.googleapis.com/css2?family=Arimo:wght@400;700&display=swap" rel="stylesheet">
<style>
  :root {
    --page-bg: #e9e9e8;
    --card-white: #fbfbfa;
    --royal-blue: #2a3bc4;
    --deep-blue: #141a6b;
    --bright-blue: #3a4fe0;
    --gold: #c8952e;
    --gold-light: #e2b85a;
    --ink-blue: #2432a8;
    --hill-white: #f1f1f1;
  }
  * { box-sizing: border-box; margin: 0; padding: 0; }
  html, body { width: 1200px; height: 801px; overflow: hidden; }
  body {
    background: var(--page-bg);
    font-family: "Arimo", Arial, sans-serif;
    display: flex;
    align-items: center;
    justify-content: center;
    gap: 40px;
  }
  .card {
    width: 520px;
    height: 297px;
    position: relative;
    overflow: hidden;
    box-shadow: 0 6px 18px rgba(0,0,0,0.18);
  }

  /* Front: contact side */
  .card-front { background: var(--card-white); }
  .brand-name {
    font-weight: 700;
    line-height: 1;
    white-space: nowrap;
  }
  .front-brand {
    position: absolute;
    left: 130px;
    top: 70px;
    color: var(--ink-blue);
    font-size: 30px;
  }
  .person {
    position: absolute;
    left: 30px;
    top: 160px;
    width: 240px;
    text-align: right;
  }
  .person-name {
    color: var(--gold);
    font-weight: 700;
    font-size: 19px;
    letter-spacing: 0.5px;
    white-space: nowrap;
  }
  .person-role { color: var(--ink-blue); font-size: 14px; margin-top: 4px; }
  .divider {
    position: absolute;
    left: 288px;
    top: 140px;
    width: 1px;
    height: 66px;
    background: var(--ink-blue);
  }
  .contact-list {
    position: absolute;
    left: 304px;
    top: 138px;
    list-style: none;
  }
  .contact-item {
    display: flex;
    align-items: center;
    gap: 8px;
    color: var(--ink-blue);
    font-size: 13px;
    line-height: 23px;
    white-space: nowrap;
  }
  .contact-icon { width: 13px; height: 13px; flex: none; }
  .address {
    position: absolute;
    left: 0;
    right: 0;
    bottom: 30px;
    text-align: center;
    color: var(--ink-blue);
    font-size: 14px;
  }

  /* Back: brand side */
  .card-back {
    background: radial-gradient(ellipse at 52% 55%, var(--bright-blue) 0%, var(--royal-blue) 40%, var(--deep-blue) 100%);
  }
  .back-brand {
    position: absolute;
    left: 40px;
    top: 118px;
  }
  .back-brand .brand-name { color: #ffffff; font-size: 32px; }
  .tagline {
    margin-top: 12px;
    color: var(--gold-light);
    font-size: 14px;
    white-space: nowrap;
  }
  .hill-scene {
    position: absolute;
    right: 0;
    top: 0;
    width: 260px;
    height: 297px;
  }
</style>
</head>
<body>

  <section class="card card-front" aria-label="Business card front">
    <div class="front-brand brand-name">Harbor Stone Church</div>

    <div class="person">
      <div class="person-name">DANIEL MARSH</div>
      <div class="person-role">Manager</div>
    </div>

    <div class="divider"></div>

    <ul class="contact-list">
      <li class="contact-item">
        <svg class="contact-icon" viewBox="0 0 16 16"><circle cx="8" cy="8" r="8" fill="var(--gold-light)"/><path d="M5 4.5c.6-.4 1.2 0 1.4.6l.4 1c.1.4 0 .7-.3.9l-.4.3c.4.9 1.1 1.6 2 2l.3-.4c.2-.3.6-.4.9-.3l1 .4c.6.2 1 .8.6 1.4-.5.8-1.4 1.1-2.3.8C6.8 10.5 5.5 9.2 4.8 7.4c-.3-.9 0-2.1.2-2.9z" fill="#fff"/></svg>
        <span>555-018-2100</span>
      </li>
      <li class="contact-item">
        <svg class="contact-icon" viewBox="0 0 16 16"><rect x="1" y="3.5" width="14" height="9" rx="1" fill="var(--gold)"/><path d="M1.5 4l6.5 5 6.5-5" fill="none" stroke="#fff" stroke-width="1.2"/></svg>
        <span>office@harborstone.org</span>
      </li>
      <li class="contact-item">
        <svg class="contact-icon" viewBox="0 0 16 16"><circle cx="8" cy="8" r="7" fill="var(--gold)"/><g fill="none" stroke="#fff" stroke-width="1"><circle cx="8" cy="8" r="4.5"/><path d="M3.5 8h9M8 3.5c-2 2.5-2 6.5 0 9M8 3.5c2 2.5 2 6.5 0 9"/></g></svg>
        <span>www.harborstone.org</span>
      </li>
    </ul>

    <p class="address">Your address, city, state, ZIP 0000</p>
  </section>

  <section class="card card-back" aria-label="Business card back">
    <div class="back-brand">
      <div class="brand-name">Harbor Stone Church</div>
      <p class="tagline">Love God. Love people. Follow Jesus.</p>
    </div>

    <svg class="hill-scene" viewBox="0 0 260 297" role="img" aria-label="Illustration of a large white cross standing on a hilltop">
      <path d="M40 297 C 90 250, 110 190, 150 170 C 190 160, 230 170, 260 165 L 260 297 Z" fill="var(--hill-white)"/>
    </svg>
  </section>

</body>
</html>
```